Web Design For Calloway Pool Service

We are working with a company that wants a website for their pool service. Some sites to use for content/competitors and inspiration:
https://sacramento.brimwaterpools.example/builder/newbuild/repair/ppc
https://coralbaypoolcareandmore.example/
https://lumoxpoolservice.example/
https://www.halvorsenspoolresurfacing.example/pool-renovation-ga/
Thank you for taking the time to consider designing a website for us. We are web developers based in Stockton, CA, USA. Most of our projects go through the same process. Understanding this process may help you win a project with us. We custom-code all of our websites in-house. We don’t have any requirements as to what tools you use for your design, but we prefer Figma files. For any design that we label as four-stars, we send it to the client for review. The client picks the final design they want us to use. Once we complete this process, we will continue to show additional clients all the four-star sites and purchase them later. Your designs will have multiple chances to sell. For better chances of success, we ask that you follow these guidelines.
IMAGES:
If you use any images or icons in the design, we ask that you have a link to the asset so we can purchase the image/icon. Most of the designs we submit do not have the customer’s images on them unless they have some great images. Be creative; show us the feeling you are trying to portray with your image choices. Use any royalty-free site you choose. We subscribe to Adobe and mainly use their images, but we can purchase images outside of Adobe. PLEASE NOTE: we will not submit designs to clients with watermarks on the images.
FONTS:
We ask that you identify the fonts used in the design. This can be done in a message if you want. We typically use Google Fonts and Adobe Fonts.
CONTENT:
We're always open to different content and ideas. We often submit designs with stock images so the client can see our vision. We typically take pictures after the website launch to use their images with our vision. Lorem Ipsum is fine for paragraphs, but we ask that you write the headers in correct English. We want to be able to show the vision and identify the sections of the website.
INSPIRATION:
We typically add a couple of links in the brief of websites we like to help you get started in your design.
REVISIONS:
We do not often ask for revisions of the designs unless we see something in the design that may not appeal to the client. If there are slight changes that we want to make, we do that in the development process.
FEEDBACK:
We rarely give feedback on designs during the design process. We are working on many website projects and do not have the time to provide feedback. We usually respond if your request is well thought out and asks specific questions, but a note asking “feedback, please” usually goes unanswered.

```html
<!DOCTYPE html>
<html lang="en">
<head>
<meta charset="utf-8">
<title>Calloway Pool Service</title>
<link rel="stylesheet" href="https://fonts.googleapis.com/css2?family=Poppins:wght@300;400;500;600;700&family=Quicksand:wght@400;500;600&display=swap">
<style>
:root{
  --blue:#1b57bd;
  --blue-deep:#163f96;
  --navy:#1c3f8f;
  --accent:#5a3fc0;
  --ink:#2a2a2a;
  --text:#3c3c3c;
  --white:#ffffff;
  --footer:#060606;
  --teal:#2bb8d2;
}
*{margin:0;padding:0;box-sizing:border-box}
html,body{width:1200px;height:5000px;overflow:hidden}
body{position:relative;background:var(--white);font-family:"Quicksand",sans-serif;color:var(--text)}
.abs{position:absolute}
.btn{position:absolute;display:flex;align-items:center;gap:10px;height:42px;padding:0 14px 0 18px;border-radius:21px;background:var(--navy);color:var(--white);font:500 14px "Poppins",sans-serif;letter-spacing:.3px}
.btn .dot{width:18px;height:18px;border-radius:50%;background:var(--white);display:flex;align-items:center;justify-content:center}
.btn .dot::after{content:"";border-left:6px solid var(--navy);border-top:4px solid transparent;border-bottom:4px solid transparent;margin-left:2px}
.photo{position:absolute}
.heading{font:300 40px "Poppins",sans-serif;color:var(--ink)}
.heading b{font-weight:700}
.rule{position:absolute;width:58px;height:5px;background:var(--accent)}
.para{font:500 15.5px/27px "Quicksand",sans-serif;text-align:justify;color:var(--text)}

/* hero */
.hero{position:absolute;left:0;top:0;width:1200px;height:720px;overflow:hidden}
.hero-bg{position:absolute;inset:0;background:linear-gradient(180deg,#3e5f3a 0%,#5c7b48 35%,#4f8e6a 52%,#2fa8b8 68%,#1fa7c5 100%)}
.hero-shade{position:absolute;inset:0;background:rgba(10,30,40,.18)}
.brand{position:absolute;left:115px;top:28px;font:500 30px "Poppins",sans-serif;color:var(--white);letter-spacing:1px}
.brand-ring{position:absolute;left:112px;top:18px;width:24px;height:24px;border:2px solid var(--white);border-radius:50%}
.nav{position:absolute;top:102px;left:352px;display:flex;gap:40px;font:500 14px "Poppins",sans-serif;color:var(--white)}
.nav .active{color:#5aa8ff}
.nav-line{position:absolute;top:86px;left:340px;width:748px;height:1px;background:rgba(255,255,255,.6)}
.nav-mark{position:absolute;top:84px;left:352px;width:46px;height:4px;background:var(--blue);border-radius:2px}
.social-ring{position:absolute;top:20px;left:884px;width:46px;height:46px;border-radius:50%;border:2px solid var(--blue);background:rgba(27,87,189,.25)}
.hero h1{position:absolute;top:252px;left:0;width:1200px;text-align:center;font:700 50px "Poppins",sans-serif;color:var(--white)}
.hero .lead{position:absolute;top:330px;left:250px;width:700px;text-align:center;font:500 19px/30px "Poppins",sans-serif;color:var(--white)}
.dots{position:absolute;display:flex;gap:10px}
.dots span{width:12px;height:12px;border-radius:50%;border:2px solid var(--white)}
.dots .on{background:var(--white)}
.dots.dark span{border-color:var(--white)}

/* cards */
.card{position:absolute;width:310px;height:400px;background:var(--white);box-shadow:0 4px 14px rgba(0,0,0,.14);border-bottom:5px solid var(--accent)}
.card .img{height:185px}
.card .icon{position:absolute;left:127px;top:154px;width:58px;height:58px;border-radius:50%;background:var(--white);border:2px solid var(--navy);display:flex;align-items:center;justify-content:center}
.card .icon i{width:26px;height:22px;border:2px solid var(--navy);border-radius:4px}
.card h3{position:absolute;top:220px;width:100%;text-align:center;font:600 23px "Poppins",sans-serif;color:var(--blue)}
.card .bar{position:absolute;top:262px;left:128px;width:54px;height:4px;background:var(--accent)}
.card p{position:absolute;top:280px;left:28px;width:254px;text-align:center;font:500 13px/21px "Quicksand",sans-serif;color:#555}
.card .more{position:absolute;top:350px;width:100%;text-align:center;font:500 13px "Quicksand",sans-serif;color:var(--accent);text-decoration:underline}

/* testimonials */
.quote-card{position:absolute;left:112px;top:3578px;width:976px;height:222px;background:var(--white);border-radius:10px}
.side-card{position:absolute;top:3578px;width:82px;height:222px;background:rgba(255,255,255,.25);border-radius:10px}
.qmark{position:absolute;font:700 90px/1 "Poppins",sans-serif;color:#8d8bc9}

/* footer */
.footer{position:absolute;left:0;top:4580px;width:1200px;height:350px;background:var(--footer)}
.fcol h4{font:600 16px "Poppins",sans-serif;color:var(--white);letter-spacing:.5px}
.fcol .fr{width:52px;height:2px;background:var(--blue);margin:8px 0 18px}
.fcol li{list-style:none;font:500 12.5px/26px "Poppins",sans-serif;color:var(--white)}
.vline{position:absolute;top:4555px;width:1px;height:375px;background:rgba(255,255,255,.25)}
.contact-row{position:absolute;display:flex;gap:16px;align-items:flex-start}
.circ{width:34px;height:34px;border-radius:50%;border:2px solid var(--white);display:flex;align-items:center;justify-content:center;flex:none}
.contact-row small{display:block;font:400 12px "Poppins",sans-serif;color:#bbb}
.contact-row span{font:500 13px/20px "Poppins",sans-serif;color:var(--white)}
.copy{position:absolute;left:0;top:4930px;width:1200px;height:70px;background:var(--blue);color:var(--white);font:400 13px "Poppins",sans-serif;text-align:center;line-height:70px;letter-spacing:.5px}
.top-btn{position:absolute;left:1114px;top:4900px;width:40px;height:40px;border:2px solid var(--white);border-radius:8px;background:var(--blue);display:flex;align-items:center;justify-content:center}
</style>
</head>
<body>

<!-- Hero -->
<section class="hero">
  <div class="hero-bg" role="img" aria-label="Resort swimming pool surrounded by palm trees and lounge chairs"></div>
  <div class="hero-shade"></div>
  <div class="brand">Calloway Pool Service</div>
  <div class="social-ring"></div>
  <div class="btn" style="left:942px;top:22px;height:44px">CONTACT US <span class="dot"></span></div>
  <div class="nav-line"></div>
  <div class="nav-mark"></div>
  <nav class="nav">
    <span class="active">HOME</span><span>ABOUT</span><span>CONSULTING</span><span>POOL CONSTRUCTION</span><span>POOL MAINTENANCE</span><span>GALLERY</span>
  </nav>
  <h1>Calloway Pool Service</h1>
  <p class="lead">Perspiciatis unde omnis iste natus error sit voluptatem accusantium doloremque laudantium, totamrem aperiaminventore</p>
  <div class="btn" style="left:527px;top:412px">GET STARTED <span class="dot"></span></div>
  <div class="dots" style="left:522px;top:626px"><span></span><span class="on"></span><span></span><span></span><span></span></div>
  <svg class="abs" style="left:0;top:610px" width="1200" height="110" viewBox="0 0 1200 110">
    <path d="M0 70 C150 40 250 100 420 80 C600 58 700 20 880 55 C1000 78 1100 80 1200 40 V110 H0Z" fill="var(--blue)"/>
    <path d="M0 88 C160 60 260 110 430 96 C610 80 710 44 890 74 C1010 94 1100 96 1200 64 V110 H0Z" fill="var(--white)"/>
    <path d="M0 98 C170 75 270 112 440 106 C620 98 720 66 900 90 C1020 106 1110 104 1200 84 V110 H0Z" fill="var(--white)"/>
  </svg>
</section>

<!-- About -->
<section>
  <div class="photo" style="left:112px;top:826px;width:462px;height:436px;border-radius:10px;background:linear-gradient(180deg,#5aa8e0 0%,#4f9a5a 38%,#33c4d6 60%,#19b8d8 100%)" role="img" aria-label="Tropical resort pool with umbrellas and palm trees"></div>
  <div class="photo" style="left:427px;top:1134px;width:183px;height:182px;border-radius:10px;border:4px solid var(--white);background:linear-gradient(160deg,#6b5a45 0%,#8c7a5c 45%,#3fb0b5 100%)" role="img" aria-label="Pool cabana with wooden pergola"></div>
  <h2 class="heading abs" style="left:619px;top:844px">ABOUT <b>US</b></h2>
  <div class="rule" style="left:619px;top:904px"></div>
  <p class="para abs" style="left:619px;top:928px;width:512px">Kaerspiciatis unde omnis ikseuoste najastus error sit voluptatem accusantium doloremque laudantium, totam rem aperiam, eaque ipsa quae ab illo inventore veritatis et quasi architecto beatae vitae dicta sunt explicabo. Nemo enim ipsam voluptatem quia voluptas sit aspernatur aut odit aut fugit, sed quia consequuntur magni dolores eos qui ratione voluptatem sequi nesciunt. Neque porro quisquam est, qui dolorem ipsum quia dolor sit amet, consectetur, adipisci velit, sed quia non numquam eius modi tempora incidunt ut labore et dolore magnam</p>
  <div class="btn" style="left:625px;top:1198px">LEARN MORE <span class="dot"></span></div>
</section>

<!-- Pool care -->
<section>
  <svg class="abs" style="left:0;top:1410px" width="1200" height="80" viewBox="0 0 1200 80">
    <path d="M0 20 C140 60 300 70 460 45 C620 20 760 10 900 35 C1030 58 1120 40 1200 15 V70 C1120 90 1020 80 900 58 C760 34 620 44 460 66 C300 88 140 78 0 44Z" fill="var(--blue)"/>
  </svg>
  <div class="photo" style="left:540px;top:1460px;width:660px;height:600px;border-radius:300px 0 0 300px/240px 0 0 240px;background:linear-gradient(180deg,#f4f6f4 0%,#5f8f4f 25%,#4c7a45 45%,#5cc6dc 62%,#2fb4d4 100%)" role="img" aria-label="Modern pool with stepping stones and pergola"></div>
  <h2 class="heading abs" style="left:200px;top:1578px;width:308px;text-align:right">POOL <b>CARE</b></h2>
  <div class="rule" style="left:450px;top:1638px"></div>
  <p class="para abs" style="left:127px;top:1660px;width:380px">Kaerspiciatis unde omnis ikseuoste najastus error sit voluptatem accusantium doloremque laudantium, totam rem aperiam, eaque ipsa quae ab illo inventore veritatis et quasi architecto beatae vitae dicta sunt explicabo. Nemo enim ipsam voluptatem quia voluptas sit aspernatur aut odit aut fugit, sed quia consequuntur magni dolores eos qui ratione</p>
  <div class="btn" style="left:360px;top:1906px">LEARN MORE <span class="dot"></span></div>
  <svg class="abs" style="left:0;top:2020px" width="1200" height="70" viewBox="0 0 1200 70">
    <path d="M0 30 C200 55 380 60 560 44 C760 26 900 10 1050 20 C1120 25 1170 30 1200 28 V50 C1150 52 1080 40 960 40 C800 42 700 66 520 66 C340 66 180 54 0 44Z" fill="var(--blue)"/>
  </svg>
</section>

<!-- Design & Build -->
<section>
  <h2 class="heading abs" style="left:0;top:2205px;width:1200px;text-align:center">DESIGN &amp; <b>BUILD</b></h2>
  <div class="rule" style="left:571px;top:2262px"></div>

  <div class="card" style="left:112px;top:2302px"><div class="img" style="background:linear-gradient(160deg,#2fb7d7,#e9e4dc)" role="img" aria-label="New pool with lounge chairs"></div><div class="icon"><i></i></div><h3>New Pools</h3><div class="bar"></div><p>Saerspiciatis unde omnis iste natsaesus error sit voluptatem accusan tiusaseem doloremque laudantiumotam.</p><div class="more">Learn More</div></div>
  <div class="card" style="left:445px;top:2302px"><div class="img" style="background:linear-gradient(180deg,#3a3a38,#8a7a66 55%,#c9c4bb)" role="img" aria-label="Pool under masonry construction"></div><div class="icon"><i></i></div><h3>Masonry</h3><div class="bar"></div><p>Saerspiciatis unde omnis iste natsaesus error sit voluptatem accusan tiusaseem doloremque laudantiumotam.</p><div class="more">Learn More</div></div>
  <div class="card" style="left:778px;top:2302px"><div class="img" style="background:linear-gradient(170deg,#d7dad8,#4da0b8 50%,#1f9ac4)" role="img" aria-label="Pool with fountain jets"></div><div class="icon"><i></i></div><h3>Smart Controls</h3><div class="bar"></div><p>Saerspiciatis unde omnis iste natsaesus error sit voluptatem accusan tiusaseem doloremque laudantiumotam.</p><div class="more">Learn More</div></div>

  <div class="card" style="left:112px;top:2740px"><div class="img" style="background:linear-gradient(160deg,#9fb3bf,#3e8bb4 55%,#1d6ea8)" role="img" aria-label="Pool ladder in blue water"></div><div class="icon"><i></i></div><h3>Lighting</h3><div class="bar"></div><p>Saerspiciatis unde omnis iste natsaesus error sit voluptatem accusan tiusaseem doloremque laudantiumotam.</p><div class="more">Learn More</div></div>
  <div class="card" style="left:445px;top:2740px"><div class="img" style="background:linear-gradient(180deg,#3b3934,#6f675a 55%,#8d8270)" role="img" aria-label="Pool renovation work site"></div><div class="icon"><i></i></div><h3>Rennovations</h3><div class="bar"></div><p>Saerspiciatis unde omnis iste natsaesus error sit voluptatem accusan tiusaseem doloremque laudantiumotam.</p><div class="more">Learn More</div></div>
  <div class="card" style="left:778px;top:2740px"><div class="img" style="background:linear-gradient(150deg,#1e5fd0,#3f86e6 55%,#e4a0a0)" role="img" aria-label="Tiled pool with steel ladder"></div><div class="icon"><i></i></div><h3>Landcaping</h3><div class="bar"></div><p>Saerspiciatis unde omnis iste natsaesus error sit voluptatem accusan tiusaseem doloremque laudantiumotam.</p><div class="more">Learn More</div></div>

  <div class="btn" style="left:527px;top:3170px">VIEW MORE <span class="dot"></span></div>
</section>

<!-- Testimonials -->
<section>
  <svg class="abs" style="left:0;top:3310px" width="1200" height="660" viewBox="0 0 1200 660" role="img" aria-label="Blue band with faint palm tree backdrop">
    <path d="M0 40 C200 10 350 20 520 40 C700 62 900 20 1200 35 V630 C1000 600 850 650 650 640 C450 630 300 600 0 625Z" fill="var(--blue)"/>
    <path d="M0 20 C200 -5 350 5 520 25 C700 45 900 5 1200 18" fill="none" stroke="var(--blue)" stroke-width="8"/>
    <path d="M0 640 C300 612 450 645 650 652 C850 660 1000 615 1200 640" fill="none" stroke="var(--blue)" stroke-width="6"/>
  </svg>
  <h2 class="heading abs" style="left:0;top:3482px;width:1200px;text-align:center;color:var(--white)">TESTIMONIALS</h2>
  <div class="abs" style="left:571px;top:3540px;width:58px;height:5px;background:var(--white)"></div>
  <div class="side-card" style="left:0"></div>
  <div class="side-card" style="left:1112px"></div>
  <div class="quote-card">
    <div class="qmark" style="left:96px;top:12px">&ldquo;</div>
    <div class="qmark" style="left:820px;top:40px">&rdquo;</div>
    <div class="abs" style="left:0;top:30px;width:976px;text-align:center;font:600 21px 'Poppins',sans-serif;color:var(--blue)">Dana Whitfield</div>
    <div class="abs" style="left:0;top:62px;width:976px;text-align:center;font:500 14px 'Quicksand',sans-serif;color:#666">Harbor Pool Covers</div>
    <p class="abs" style="left:60px;top:100px;width:856px;text-align:center;font:italic 500 13px/23px 'Quicksand',sans-serif;color:#555">"Perspiciatis unde omnis iste natus error sit voluptatem accusantium doloremque laudantium, totam rem aperiam, eaque ipsa quae ab illo inventore veritatis et quasi architecto beatae vitae dicta sunt explicabo. Nemo enim ipsam voluptatem quia voluptas sit aspernatur aut odit aut fugit, sed quia consequuntur magni dolores eos qui ratione voluptatem sequi nesciunt. Neque porro quisquam est, qui dolorem ipsum quia dolor sit amet, consectetur, adipisci velit, sed quia"</p>
  </div>
  <div class="dots" style="left:560px;top:3832px"><span></span><span class="on"></span><span></span><span></span></div>
</section>

<!-- Social feed -->
<section>
  <h2 class="heading abs" style="left:0;top:4046px;width:1200px;text-align:center">SOCIAL FEED</h2>
  <div class="rule" style="left:571px;top:4104px;background:var(--navy)"></div>
  <div class="photo" style="left:0;top:4152px;width:200px;height:216px;border-radius:8px;background:linear-gradient(180deg,#b9c6c9,#6b8a5a 50%,#48b8c8)" role="img" aria-label="Backyard pool with pergola"></div>
  <div class="photo" style="left:225px;top:4152px;width:235px;height:216px;border-radius:8px;background:linear-gradient(180deg,#6b5036,#4f7a3a 50%,#58b6c7)" role="img" aria-label="Garden lap pool"></div>
  <div class="photo" style="left:483px;top:4152px;width:235px;height:216px;border-radius:8px;background:linear-gradient(180deg,#2b3a2e,#3f6a60 50%,#2a8ea2)" role="img" aria-label="Pool at dusk"></div>
  <div class="abs" style="left:570px;top:4230px;width:60px;height:60px;border-radius:50%;border:4px solid var(--white)"></div>
  <div class="photo" style="left:742px;top:4152px;width:235px;height:216px;border-radius:8px;background:linear-gradient(180deg,#d77a86,#8a6a8a 45%,#2b9fd6)" role="img" aria-label="Infinity pool at sunset"></div>
  <div class="photo" style="left:1000px;top:4152px;width:200px;height:216px;border-radius:8px;background:linear-gradient(180deg,#e9ecee,#5a6a6a 50%,#5bb5d6)" role="img" aria-label="Modern house with pool"></div>
  <div class="btn" style="left:527px;top:4398px">VIEW MORE <span class="dot"></span></div>
</section>

<!-- Footer -->
<svg class="abs" style="left:0;top:4500px" width="1200" height="90" viewBox="0 0 1200 90">
  <path d="M0 40 C200 10 380 30 560 50 C760 70 950 20 1200 40 V90 H0Z" fill="var(--blue)"/>
  <path d="M0 62 C220 36 400 50 580 66 C780 84 960 44 1200 60 V90 H0Z" fill="var(--footer)"/>
</svg>
<footer class="footer">
  <div class="abs" style="left:150px;top:108px;font:500 34px 'Poppins',sans-serif;color:var(--blue);width:300px;line-height:40px">Calloway Pool Service</div>
  <div class="abs" style="left:258px;top:200px;width:46px;height:46px;border-radius:50%;border:2px solid var(--white)"></div>
  <div class="fcol abs" style="left:472px;top:92px"><h4>LINKS</h4><div class="fr"></div><ul><li>HOME</li><li>ABOUT</li><li>CONSULTING</li><li>POOL CONSTRUCTION</li><li>POOL MAINTENANCE</li><li>GALLERY</li></ul></div>
  <div class="fcol abs" style="left:675px;top:92px"><h4>SUPPORT</h4><div class="fr"></div><ul><li>TEAM</li><li>ABOUT US</li><li>CAREERS</li><li>OUR VALUES</li></ul></div>
  <div class="fcol abs" style="left:862px;top:92px"><h4>CONTACT US</h4><div class="fr"></div></div>
  <div class="contact-row" style="left:855px;top:140px"><div class="circ"><svg width="14" height="18" viewBox="0 0 14 18"><path d="M7 1a6 6 0 0 0-6 6c0 4 6 10 6 10s6-6 6-10a6 6 0 0 0-6-6z" fill="#fff"/><circle cx="7" cy="7" r="2.2" fill="#060606"/></svg></div><div><small>Address</small><span>41 Linden Court,<br>Fair Haven, NJ 07704</span></div></div>
  <div class="contact-row" style="left:855px;top:218px"><div class="circ"><svg width="16" height="16" viewBox="0 0 16 16"><path d="M3 1l3 3-2 2c1 2 3 4 5 5l2-2 3 3-2 2C7 14 2 9 1 3z" fill="#fff"/></svg></div><div><small>Call Us</small><span>1-800-555-0142</span></div></div>
  <div class="contact-row" style="left:855px;top:278px"><div class="circ"><svg width="16" height="12" viewBox="0 0 16 12"><rect x="1" y="1" width="14" height="10" fill="none" stroke="#fff" stroke-width="1.6"/><path d="M1 1l7 6 7-6" fill="none" stroke="#fff" stroke-width="1.6"/></svg></div><div><small>Email</small><span>info@callowaypool.example</span></div></div>
</footer>
<div class="vline" style="left:450px"></div>
<div class="vline" style="left:650px"></div>
<div class="vline" style="left:830px"></div>
<div class="copy">© 2024. ALL RIGHTS RESERVED.</div>
<div class="top-btn"><svg width="14" height="10" viewBox="0 0 14 10"><path d="M2 8l5-5 5 5" fill="none" stroke="#fff" stroke-width="2"/></svg></div>

</body>
</html>
```